Business Card Design Harbourline Flooring

We are a Mobile Flooring Company servicing the Central Coast NSW and Newcastle.We sell and Install Bamboo flooring, laminate flooring and engineered flooring to do it yourself renovators, builders and home improvement clientsOur prices are very competitive and we have a great colour range and selection.We would like the front of the card to have the wood floorboard image (perhaps as the background) and then have our logo over the top (large) with the logo in spot gloss and all the writing in spot gloss. Details of what we do can be included on the back with the deer image (perhaps in silhouette) in the background. Any other ideas using these images will be appreciated.

Target Market(s)

DIY renovators, builders, home improvement clients

Industry/Entity Type

Flooring

Contact Information for Business Card

Servicing Central Coast to Newcastle
sales@harbourlineflooring.com.au
0438 162 504
www.harbourlineflooring.com.au

Font styles to use
Other font styles liked:
• You decide

Requirements
Must have
• The project must have both files uploaded on the business card the image of the woodland forest/ floorboards in the background - filling the whole business card or half business card with the logo over the top
• The logo and all the writing needs to be spot gloss
Nice to have
• A clear easy to read attractive business card
Should not have
• Too dark

```html
<!DOCTYPE html>
<html lang="en">
<head>
<meta charset="utf-8">
<title>Harbourline Flooring – Business Card</title>
<link rel="stylesheet" href="https://fonts.googleapis.com/css2?family=Almendra&family=PT+Sans:wght@400;700&display=swap">
<style>
  :root {
    --page: #ffffff;
    --label: #222222;
    --band-top: #fbd54a;
    --band-bottom: #f6b92c;
    --rule-red: #d8432a;
    --rule-fade: #f5c9a0;
    --brand: #1e9bc4;
    --text: #1d1a16;
    --wood-light: #f0d596;
    --wood-mid: #d9a860;
    --wood-deep: #b9793b;
    --deer: #b98252;
  }
  * { margin: 0; padding: 0; box-sizing: border-box; }
  html, body { width: 1200px; height: 411px; overflow: hidden; background: var(--page); }
  .sheet { position: relative; width: 1200px; height: 411px; }

  .side-label {
    position: absolute; top: 2px;
    font-family: "Almendra", serif; font-size: 40px; color: var(--label);
  }
  .side-label--back { left: 232px; }
  .side-label--front { left: 852px; }

  .card {
    position: absolute; top: 55px; height: 350px; overflow: hidden;
    font-family: "PT Sans", sans-serif; color: var(--text);
  }
  .card--back { left: 0; width: 596px; }
  .card--front { left: 621px; width: 579px; }

  .card__header {
    position: absolute; left: 0; top: 0; width: 100%; height: 74px;
    background: linear-gradient(to bottom, var(--band-top), var(--band-bottom));
    display: flex; align-items: center; gap: 14px; padding-left: 22px;
  }
  .brand-dot { width: 26px; height: 26px; border-radius: 50%; background: var(--rule-red); }
  .brand-name { font-family: "Almendra", serif; font-size: 34px; color: var(--brand); }
  .card__rule {
    position: absolute; left: 0; top: 74px; width: 100%; height: 12px;
    background: linear-gradient(to right, var(--rule-red) 20%, var(--rule-fade) 75%, rgba(255,255,255,0.6));
  }

  .card__photo { position: absolute; left: 0; top: 86px; width: 100%; bottom: 0; }
  .card--back .card__photo {
    background: linear-gradient(160deg, var(--wood-mid) 0%, var(--wood-light) 45%, var(--wood-mid) 75%, var(--wood-deep) 100%);
  }
  .card--front .card__photo {
    background: radial-gradient(ellipse at 62% 55%, var(--wood-light) 0%, var(--wood-mid) 55%, var(--wood-deep) 100%);
  }
  .card__art {
    position: absolute; left: 8px; top: 80px; width: 150px; height: 265px;
    background: linear-gradient(to bottom, var(--deer), #9c6a3f);
    border-radius: 40px 40px 10px 10px; opacity: 0.85;
  }

  .back-copy {
    position: absolute; right: 64px; top: 204px;
    text-align: right; font-size: 17px; line-height: 23.5px;
  }

  .front-copy { position: absolute; left: 30px; top: 106px; font-size: 18px; line-height: 24px; }
  .front-copy__area { font-weight: 700; text-decoration: underline; }
  .front-copy__pitch { padding-left: 20px; }
  .front-copy__points { padding-left: 48px; }
  .contact { margin-top: 14px; line-height: 25px; }
</style>
</head>
<body>
<main class="sheet">
  <div class="side-label side-label--back">Back</div>
  <div class="side-label side-label--front">Front</div>

  <section class="card card--back">
    <div class="card__photo" role="img" aria-label="Warm photo of a room with light timber floorboards"></div>
    <header class="card__header">
      <span class="brand-dot"></span>
      <span class="brand-name">Harbourline Flooring</span>
    </header>
    <div class="card__rule"></div>
    <div class="card__art" role="img" aria-label="Illustration of a spotted deer standing"></div>
    <p class="back-copy">
      We sell and Install Bamboo flooring,<br>
      laminate flooring and engineered flooring<br>
      to do it yourself renovators,<br>
      builders and home improvement clients<br>
      Our prices are very competitive<br>
      and we have a great colour range and selection.
    </p>
  </section>

  <section class="card card--front">
    <div class="card__photo" role="img" aria-label="Photo of a timber floor with a star inlay"></div>
    <header class="card__header">
      <span class="brand-dot"></span>
      <span class="brand-name">Harbourline Flooring</span>
    </header>
    <div class="card__rule"></div>
    <div class="front-copy">
      <p class="front-copy__area">Servicing the Central Coast NSW and Newcastle</p>
      <p class="front-copy__pitch">More than just floor, we give more adventage</p>
      <p class="front-copy__points">- High quality &nbsp;- Low Price - great colour</p>
      <div class="contact">
        <p>Contact :</p>
        <p>0438 162 504</p>
        <p>www.harbourlineflooring.com.au</p>
        <p>sales@harbourlineflooring.com.au</p>
      </div>
    </div>
  </section>
</main>
</body>
</html>
```